Criação de Kit Layout de Posts para Redes Sociais (Facebook, Instagram e etc) para Construção & Engenharia
A empresa queria:
" TRABALHAMOS COM LOCAÇÃO, VENDA DE EQUIPAMENTOS, MONTAGEM E PROJETOS DE ANDAIME E ESCORAMENTO "

```html
<!DOCTYPE html>
<html lang="pt-BR">
<head>
<meta charset="UTF-8">
<title>Vanto Equipamentos – Mais segurança para sua obra</title>
<link href="https://fonts.googleapis.com/css2?family=Oswald:wght@500;600&family=Montserrat:wght@500;700;800&display=swap" rel="stylesheet">
<style>
  :root {
    --yellow: #f5c21b;
    --yellow-soft: #f7d65a;
    --ink: #232323;
    --gray: #5a5a5a;
    --paper: #f4f4f4;
    --paper-edge: #e6e6e6;
  }
  * { margin: 0; padding: 0; box-sizing: border-box; }
  html, body { width: 1200px; height: 1200px; overflow: hidden; }
  body { background: var(--paper); }
  .post {
    position: relative;
    width: 1200px;
    height: 1200px;
    overflow: hidden;
    background: radial-gradient(circle at 30% 40%, #ffffff 0%, var(--paper) 55%, var(--paper-edge) 100%);
  }
  .shapes { position: absolute; inset: 0; }
  .headline {
    position: absolute;
    left: 34px;
    top: 238px;
    font-family: "Oswald", sans-serif;
    font-weight: 600;
    font-size: 78px;
    line-height: 92px;
    color: var(--ink);
    text-transform: uppercase;
    letter-spacing: -0.5px;
  }
  .brand {
    position: absolute;
    left: 216px;
    top: 992px;
    display: flex;
    align-items: center;
    gap: 22px;
  }
  .brand-square {
    width: 110px;
    height: 110px;
    background: var(--yellow);
  }
  .brand-name {
    font-family: "Montserrat", sans-serif;
    font-weight: 800;
    font-size: 64px;
    line-height: 1;
    color: var(--ink);
    letter-spacing: 2px;
  }
  .brand-tag {
    font-family: "Montserrat", sans-serif;
    font-weight: 500;
    font-size: 27px;
    color: var(--gray);
    letter-spacing: 5px;
    margin-top: 12px;
  }
  .partners {
    position: absolute;
    left: 216px;
    top: 1128px;
    font-family: "Montserrat", sans-serif;
    font-weight: 700;
    font-size: 24px;
    color: var(--ink);
    letter-spacing: 0.5px;
  }
</style>
</head>
<body>
<main class="post">
  <svg class="shapes" width="1200" height="1200" viewBox="0 0 1200 1200">
    <defs>
      <linearGradient id="photoTone" x1="0" y1="0" x2="1" y2="1">
        <stop offset="0" stop-color="#f8e27a"/>
        <stop offset="0.5" stop-color="#f3cc2e"/>
        <stop offset="1" stop-color="#c9a227"/>
      </linearGradient>
    </defs>
    <polygon class="corner-top" points="0,0 125,0 0,120" fill="var(--yellow)"/>
    <polygon class="corner-bottom" points="0,1020 0,1200 170,1200" fill="var(--yellow)"/>
    <polygon class="photo-area" role="img" aria-label="Foto de um trabalhador sorridente de capacete amarelo e camisa xadrez, de braços cruzados, em frente a uma obra em tons amarelos" points="1200,48 456,696 984,1200 1200,1200" fill="url(#photoTone)"/>
    <polyline class="frame-line" points="1150,0 427,696 950,1200" fill="none" stroke="var(--ink)" stroke-width="12"/>
  </svg>

  <h1 class="headline">Mais<br>Segurança<br>para sua obra!</h1>

  <div class="brand">
    <div class="brand-square"></div>
    <div class="brand-text">
      <div class="brand-name">VANTO</div>
      <div class="brand-tag">EQUIPAMENTOS</div>
    </div>
  </div>
  <p class="partners">ALTIVA ANDAIMES | FERRAMAQ</p>
</main>
</body>
</html>
```